Wholesale company needs a sales brochure for our latest gadget- Nimbo Pebble. We sell to retailers

We need a sale brochure for our new product- Nimbo/Dart Pebble. It's an elegant little device that connects to any smartphone using an APP and let you locate your keys or your phone when you can't find them. We would like to see a design that uses the colors: Light blue, Black and metallic silver. The final design should communicate tech and innovative product. We need a total of 4 pages of 8.5x11'' (US letter size) to describe:
- Product benefits
- Product in use
- Display solution
- Profit generator
- Success story

Attached below are photos of the packaging and the display for your reference. Better photos will be sent later.
Please keep in mind that this product should be displayed on the counter with high foot traffic OR hang on hooks on a display fixture in the store.

This brochure will be used mainly to be sent digitally via email BUT we will also print it and will be mailing copies to our buyers.

Target Market(s)

Retailers and Distributors.
Small to mid-size retail stores:
- Electronic stores
- Convenient store
- Cellphone stores
- Gift stores

Industry/Entity Type

Retail

Font styles to use
Sans Serif

Colors
0692cd
ffffff
f3f1f8
33a6d7
85cae6

Requirements
Must have
• Must have:
• - "techie" and innovative look to go hand in hand with the product itself.
• - "in use" photos
• - "Description of the product"
• - Spec info
Nice to have
• Pattern or abstract design on background behind the text and images

```html
<!DOCTYPE html>
<html lang="en">
<head>
<meta charset="utf-8">
<title>Nimbo Pebble Brochure</title>
<link rel="stylesheet" href="https://fonts.googleapis.com/css2?family=Roboto+Condensed:wght@300;400;700&family=Roboto:wght@300&display=swap">
<style>
:root{
  --stage:#4a4a4a;
  --blue:#0692cd;
  --blue-mid:#33a6d7;
  --blue-light:#85cae6;
  --sky:#1fb3ef;
  --violet:#b36cf0;
  --white:#ffffff;
  --mist:#f3f1f8;
  --ink:#1a1a1a;
  --accent:#2a64c8;
  --magenta:#c0307f;
  --silver:#c9cdd2;
}
*{margin:0;padding:0;box-sizing:border-box}
html,body{width:947px;height:1200px;overflow:hidden;background:var(--stage)}
body{position:relative;font-family:"Roboto Condensed",sans-serif;color:var(--ink)}
.spread{position:absolute;left:89px;width:768px;height:496px;background:var(--white);overflow:hidden;box-shadow:0 4px 14px rgba(0,0,0,.45)}
.spread--outside{top:40px}
.spread--inside{top:612px}
.spread-label{position:absolute;left:0;width:947px;text-align:center;font-family:"Roboto",sans-serif;font-weight:300;font-size:27px;color:var(--white);letter-spacing:.5px}
.spread-label--outside{top:558px}
.spread-label--inside{top:1136px}
.bg{position:absolute;inset:0}
.fold{position:absolute;top:0;bottom:0;width:1px;background:rgba(0,0,0,.06)}
.abs{position:absolute}
.wordmark{position:absolute;font-weight:700;color:var(--white);letter-spacing:-.5px;line-height:1;white-space:nowrap}
.photo{position:absolute;border-radius:4px}
/* outside */
.info-box{left:89px;top:250px;width:208px;height:94px;background:var(--white);border-radius:6px;text-align:center;padding-top:16px;font-size:12px;line-height:15px;box-shadow:0 2px 8px rgba(0,0,0,.08)}
.info-box b{font-weight:700}
.info-box .url{display:block;margin-top:10px;color:var(--blue);font-weight:700;font-size:15px;letter-spacing:1px}
.contact-title{font-size:9px;color:var(--blue)}
.contact-line{font-size:7.5px;display:flex;align-items:center;gap:5px;margin-top:6px}
.contact-line strong{font-size:8.5px}
.social-grid{display:grid;grid-template-columns:repeat(3,19px);gap:6px 5px;margin-top:10px}
.social-grid span{width:19px;height:19px;border-radius:50%;background:var(--blue)}
.headline{left:428px;top:356px;font-size:40px;font-weight:400;letter-spacing:-.5px;white-space:nowrap}
.headline em{font-style:normal;font-weight:700;background:linear-gradient(90deg,#3a2a8e,var(--magenta));-webkit-background-clip:text;background-clip:text;color:transparent}
.banner{left:434px;top:404px;width:286px;height:46px}
.banner-text{left:434px;top:406px;width:286px;text-align:center;font-size:11px;line-height:15px}
.banner-text span{color:var(--blue);font-weight:700;letter-spacing:1.5px}
.tagline{left:420px;top:456px;width:314px;text-align:center;font-size:11.5px;line-height:15px;font-weight:700}
.tagline span{color:var(--accent)}
/* inside */
.chip{background:var(--white);color:var(--blue);font-weight:700;padding:2px 5px;font-size:15px}
.how-box{left:19px;top:276px;height:40px;background:var(--blue);color:var(--white);font-size:19px;font-weight:300;padding:8px 6px;white-space:nowrap}
.steps{list-style:none}
.steps li{display:flex;gap:6px;font-size:11.5px;line-height:14px}
.num{flex:none;width:10px;height:10px;border-radius:50%;background:var(--white);color:var(--blue);font-size:7px;font-weight:700;text-align:center;line-height:10px;margin-top:2px}
.steps--start li{color:var(--white);margin-bottom:13px}
.steps--how{left:20px;top:332px;width:350px}
.steps--how li{font-size:9px;line-height:12px;margin-bottom:12px}
.steps--how .num{background:var(--blue);color:var(--white)}
.steps--how b{color:var(--blue);font-weight:700}
.footer-bar{left:0;right:0;bottom:0;height:38px;background:linear-gradient(90deg,#0a78b6,var(--blue))}
.footer-note{top:470px;width:384px;text-align:center;color:var(--white);font-size:8.5px}
.footer-note b{font-weight:700}
.features-title{left:405px;top:228px;font-size:19px;font-weight:700;color:var(--blue)}
.feature{left:405px;width:145px}
.feature h3{font-size:12px;font-weight:400;color:var(--blue);display:flex;gap:12px;align-items:center}
.feature h3 i{width:10px;height:10px;background:var(--blue);display:inline-block}
.feature p{font-size:7px;line-height:9.5px;text-align:justify;margin:4px 0 0 23px}
</style>
</head>
<body>

<section class="spread spread--outside" aria-label="Brochure outside">
  <svg class="bg" viewBox="0 0 768 496" preserveAspectRatio="none" aria-hidden="true">
    <defs>
      <linearGradient id="outLeft" x1="0" y1="0" x2="1" y2="1">
        <stop offset="0" stop-color="#b36cf0"/><stop offset=".55" stop-color="#5a7cf4"/><stop offset="1" stop-color="#1fb3ef"/>
      </linearGradient>
      <linearGradient id="outRight" x1="0" y1="0" x2="1" y2="0">
        <stop offset="0" stop-color="#5a8cf4"/><stop offset=".6" stop-color="#1fb3ef"/><stop offset="1" stop-color="#2fd0b8"/>
      </linearGradient>
    </defs>
    <rect width="768" height="496" fill="#f3f1f8"/>
    <path d="M0 0H390V260C340 250 310 300 300 320C250 250 180 230 120 300C90 340 60 300 0 220Z" fill="url(#outLeft)"/>
    <path d="M390 0H768V240C720 200 640 205 600 240C540 290 470 300 390 300Z" fill="url(#outRight)"/>
  </svg>
  <div class="fold" style="left:390px"></div>

  <div class="wordmark" style="left:126px;top:162px;font-size:30px">Nimbo Pebble</div>
  <div class="abs info-box">For more in-depth<br><b>instructions</b> and <b>features</b><br>please visit<span class="url">www.nimbopebble.com</span></div>

  <div class="abs" style="left:22px;top:400px">
    <div class="contact-title">Get In Touch</div>
    <div class="contact-line"><svg width="8" height="9" viewBox="0 0 8 10"><path d="M4 0a3.5 3.5 0 0 0-3.5 3.5C.5 6 4 10 4 10s3.5-4 3.5-6.5A3.5 3.5 0 0 0 4 0Zm0 5a1.4 1.4 0 1 1 0-2.8A1.4 1.4 0 0 1 4 5Z" fill="#0692cd"/></svg>Company Address goes here</div>
    <div class="contact-line"><svg width="8" height="8" viewBox="0 0 10 10"><path d="M2 0l2 2.5-1.2 1.3a6 6 0 0 0 3.4 3.4L7.5 6 10 8 8.5 10C4 10 0 6 0 1.5Z" fill="#0692cd"/></svg><strong>0123456789</strong></div>
    <div class="contact-line"><svg width="8" height="8" viewBox="0 0 10 10"><rect x="0" y="3" width="10" height="5" fill="#0692cd"/><rect x="2" y="0" width="6" height="3" fill="#0692cd"/></svg><strong>0123456789</strong></div>
  </div>
  <div class="abs" style="left:144px;top:400px">
    <div class="contact-title">Social media</div>
    <div class="social-grid"><span></span><span></span><span></span><span></span><span></span><span></span></div>
  </div>

  <div class="wordmark" style="left:411px;top:30px;font-size:30px">Nimbo<br>Pebble</div>
  <div class="photo" role="img" aria-label="Counter display stand filled with packaged Nimbo Pebble finders and keys" style="left:527px;top:36px;width:145px;height:300px;background:linear-gradient(180deg,#2b2b2b 0 14%,#e9edf1 14% 85%,#1e1e1e 85%)"></div>

  <div class="abs headline">Find Your <em>Everything</em></div>
  <svg class="abs banner" viewBox="0 0 286 46" aria-hidden="true">
    <path d="M0 4L12 4 10 30Z" fill="#0692cd"/><path d="M286 4L274 4 276 30Z" fill="#0692cd"/>
    <rect x="8" y="36" width="270" height="4" fill="#0692cd"/>
    <line x1="40" y1="24" x2="70" y2="24" stroke="#0692cd"/><line x1="216" y1="24" x2="246" y2="24" stroke="#0692cd"/>
  </svg>
  <div class="abs banner-text">Track the things that matter to you most with our<br><span>BLUETOOTH FINDER</span></div>
  <div class="abs tagline">Just attach it to your keys, pair it with our<br><span>INTUITIVE APP AND VIOLA!</span> Lost is now <span>FOUND.</span></div>
</section>
<div class="spread-label spread-label--outside">Brochure Outside</div>

<section class="spread spread--inside" aria-label="Brochure inside">
  <svg class="bg" viewBox="0 0 768 496" preserveAspectRatio="none" aria-hidden="true">
    <defs>
      <linearGradient id="inBlue" x1="0" y1="0" x2="1" y2="1">
        <stop offset="0" stop-color="#0a7fd0"/><stop offset="1" stop-color="#1fb3ef"/>
      </linearGradient>
    </defs>
    <rect width="768" height="496" fill="#f3f1f8"/>
    <path d="M0 0H384V210C320 190 260 230 210 260C150 290 60 300 0 240Z" fill="url(#inBlue)"/>
    <path d="M384 0H768V150C700 140 660 160 620 180C560 200 470 190 384 200Z" fill="url(#inBlue)"/>
  </svg>
  <div class="fold" style="left:384px"></div>

  <div class="wordmark" style="left:29px;top:27px;font-size:30px">Nimbo Pebble</div>
  <div class="abs chip" style="left:20px;top:79px">Getting started:</div>
  <ol class="abs steps steps--start" style="left:20px;top:116px;width:205px">
    <li><span class="num">1</span>Download the free "pebblego" app</li>
    <li><span class="num">2</span><span>Turn on the device with a <b>long press</b></span></li>
    <li><span class="num">3</span><span>Open the app and press the "<b>+</b>" icon then select the Nimbo Pebble device to</span></li>
  </ol>
  <div class="photo" role="img" aria-label="Nimbo Pebble retail blister pack with a blue finder attached to keys" style="left:233px;top:26px;width:130px;height:257px;background:linear-gradient(180deg,#dfe3e7 0 12%,#1e1e1e 12% 24%,#cfd5db 24% 100%);border:1px solid #b8bec4"></div>

  <div class="abs how-box">How to use:</div>
  <ol class="abs steps steps--how">
    <li><span class="num">1</span><span><b>To locate your phone:</b> Double press the finder to activate the alaram</span></li>
    <li><span class="num">2</span><span><b>To find your keys:</b> Nagative to the "Device tab and press the "call" button</span></li>
    <li><span class="num">3</span><span><b>Selfie Remote:</b> Nagative to the "Camera" tab in the app and single press the finder to take a picture.</span></li>
    <li><span class="num">4</span><span><b>Lost record:</b> Nagative to the " Location" tab and press the"lost record" button to find the last location the device was disconnected on the map.</span></li>
  </ol>

  <div class="wordmark" style="left:409px;top:128px;font-size:26px">Nimbo Pebble</div>
  <div class="abs features-title">FEATURES</div>
  <div class="abs feature" style="top:254px"><h3><i></i>Selfie Remote</h3><p>Take group pictures and selfies with the press of a button and store the pics on your phone</p></div>
  <div class="abs feature" style="top:308px"><h3><i></i>Location Record</h3><p>Locate lost items with the Lost Record feature that provides exact coordinates of your last connected</p></div>
  <div class="abs feature" style="top:369px"><h3><i></i>Battery Tracking</h3><p>Monitor the Nimbo Pebble's battery life within the app. Never run out of juice when you need it the most! Our battery can easily be replaced</p></div>
  <div class="photo" role="img" aria-label="Open counter display box holding six packaged finders in red, white, blue and black" style="left:563px;top:100px;width:184px;height:358px;background:linear-gradient(180deg,#f4f4f4 0 22%,#1a1a1a 22% 26%,#e6e9ec 26% 90%,#111 90%)"></div>

  <div class="abs footer-bar"></div>
  <div class="abs footer-note" style="left:0">For more in-depth instructions and features, please visit: <b>www.nimbopebble.com</b></div>
  <div class="abs footer-note" style="left:384px">For more in-depth instructions and features, please visit: <b>www.nimbopebble.com</b></div>
</section>
<div class="spread-label spread-label--inside">Brochure Inside</div>

</body>
</html>
```